Criação de Layout de Post para Imóveis
A empresa queria:
" Lume Fin uma empresa especializada em soluções no segmento de crédito imobiliário. Como correspondente bancário atuamos com as principais instituições financeiras do pais, oferecemos as melhores condições para seu credito imobiliário. Nosso principal foco é buscar as melhores taxas, custos, conveniências, prazos e demais circunstâncias que melhor possa lhe atender. "

```html
<!DOCTYPE html>
<html lang="pt-BR">
<head>
<meta charset="utf-8">
<title>Lume Fin — Crédito Imobiliário</title>
<link rel="stylesheet" href="https://fonts.googleapis.com/css2?family=Barlow+Condensed:ital,wght@1,700&family=Montserrat:wght@400;500&display=swap">
<style>
  :root {
    --ink: #0b0b0b;
    --ink-soft: #1a1a1a;
    --white: #ffffff;
    --gold: #e9b94a;
    --gold-deep: #c9912c;
    --photo-light: #d9d3cf;
    --photo-mid: #b7aaa5;
    --photo-red: #d8344f;
  }
  html, body {
    margin: 0;
    padding: 0;
    width: 1200px;
    height: 1200px;
    overflow: hidden;
    background: var(--ink);
  }
  .post {
    position: relative;
    width: 1200px;
    height: 1200px;
    background: var(--ink);
    overflow: hidden;
  }
  .post__backdrop {
    position: absolute;
    inset: 0;
    width: 1200px;
    height: 1200px;
  }
  .brand {
    position: absolute;
    top: 48px;
    left: 0;
    width: 1200px;
    display: flex;
    justify-content: center;
    align-items: center;
    gap: 34px;
  }
  .brand__mark {
    width: 96px;
    height: 96px;
    border: 6px solid var(--white);
    box-sizing: border-box;
  }
  .brand__text {
    display: flex;
    flex-direction: column;
  }
  .brand__name {
    font-family: "Montserrat", sans-serif;
    font-weight: 400;
    font-size: 72px;
    line-height: 1;
    letter-spacing: 3px;
    color: var(--white);
  }
  .brand__tagline {
    margin-top: 12px;
    font-family: "Montserrat", sans-serif;
    font-weight: 500;
    font-size: 19px;
    letter-spacing: 0.5px;
    color: var(--white);
  }
  .headline {
    position: absolute;
    top: 418px;
    left: 0;
    width: 1200px;
    margin: 0;
    text-align: center;
    font-family: "Barlow Condensed", sans-serif;
    font-style: italic;
    font-weight: 700;
    color: var(--white);
    line-height: 1.08;
    text-shadow: 0 4px 18px rgba(0, 0, 0, 0.55);
  }
  .headline__line {
    display: block;
    font-size: 104px;
  }
  .headline__accent {
    background: linear-gradient(180deg, #f6d98a 0%, var(--gold) 45%, var(--gold-deep) 100%);
    -webkit-background-clip: text;
    background-clip: text;
    color: transparent;
    font-size: 118px;
  }
  .headline__line--last {
    font-size: 118px;
  }
</style>
</head>
<body>
<main class="post">
  <svg class="post__backdrop" viewBox="0 0 1200 1200" xmlns="http://www.w3.org/2000/svg">
    <defs>
      <linearGradient id="photoTone" x1="0" y1="0" x2="1" y2="1">
        <stop offset="0" stop-color="var(--photo-light)"/>
        <stop offset="0.35" stop-color="var(--photo-red)"/>
        <stop offset="0.6" stop-color="var(--photo-mid)"/>
        <stop offset="1" stop-color="#8a7c78"/>
      </linearGradient>
      <linearGradient id="cornerShade" x1="1" y1="0" x2="0.4" y2="0.6">
        <stop offset="0" stop-color="#0b0b0b" stop-opacity="1"/>
        <stop offset="1" stop-color="#0b0b0b" stop-opacity="0"/>
      </linearGradient>
      <linearGradient id="goldBand" x1="0" y1="0" x2="1" y2="0">
        <stop offset="0" stop-color="var(--gold-deep)"/>
        <stop offset="1" stop-color="var(--gold)"/>
      </linearGradient>
    </defs>
    <g role="img" aria-label="Fotografia de aperto de mãos entre cliente e corretor, com maquete de casa sobre a mesa">
      <polygon points="0,205 1200,205 1200,1080 0,1130" fill="url(#photoTone)"/>
    </g>
    <polygon points="700,205 1200,205 1200,760" fill="url(#cornerShade)"/>
    <polygon points="0,1090 560,1075 520,1145 0,1160" fill="url(#goldBand)"/>
    <polygon points="0,1140 1200,1060 1200,1200 0,1200" fill="var(--ink)"/>
  </svg>

  <header class="brand">
    <div class="brand__mark"></div>
    <div class="brand__text">
      <span class="brand__name">LUME FIN</span>
      <span class="brand__tagline">SOLUÇÕES EM CRÉDITO IMOBILIÁRIO</span>
    </div>
  </header>

  <h1 class="headline">
    <span class="headline__line">As melhores</span>
    <span class="headline__line"><span class="headline__accent">CONDIÇÕES</span> para seu</span>
    <span class="headline__line headline__line--last headline__accent">CRÉDITO IMOBILIÁRIO</span>
  </h1>
</main>
</body>
</html>
```